Trifold Brochure needed for Hearthline Counseling

Hi! We need to have a trifold brochure made.

We would like to see brochure designs that use our logo colors, which are khaki, chocolate brown, and gray.

The brochure should be a modern design and please use your creativity.

Brochure is a trifold brochure, size is 8.5 x 11 and full color.

The following attachment has the content to be used in the trifold brochure, as well as some possible pictures. I have also attached our logo.

We would like to use file #2 for sure (picture number 31759204) and add the quote from her...

"At first, I was reluctant about going to Hearthline. Once I got there, I was glad I went. I learned a lot and was treated like family the whole time." Marlene Oakes

Requirements
Must have
• Our logo
• Information should be listed exactly as the attached document
• You must stick with our logo colors

```html
<!DOCTYPE html>
<html lang="en">
<head>
<meta charset="utf-8">
<title>Hearthline Counseling – Trifold Brochure</title>
<link href="https://fonts.googleapis.com/css2?family=Raleway:wght@300;400;600&family=Open+Sans:ital,wght@0,400;0,700;1,400;1,700&display=swap" rel="stylesheet">
<style>
  :root{
    --chocolate:#5b3524;
    --rust:#8b4b2c;
    --khaki:#cdbda3;
    --gray:#8e8e8e;
    --ink:#3a3a3a;
    --paper:#ffffff;
    --backdrop:#e4e2df;
  }
  *{box-sizing:border-box;margin:0;padding:0}
  html,body{width:1200px;height:900px;overflow:hidden;background:var(--backdrop)}
  .brochure{
    position:absolute;left:45px;top:21px;width:1110px;height:858px;
    display:flex;background:var(--paper);
    box-shadow:0 6px 24px rgba(0,0,0,.18);
  }
  .panel{position:relative;width:370px;height:100%;overflow:hidden}
  .panel + .panel{border-left:1px solid rgba(0,0,0,.06)}

  /* FAQ panel */
  .panel--faq{background:linear-gradient(180deg,#f4f4f4 0%,#ffffff 40%)}
  .faq__title{
    position:absolute;left:34px;top:36px;
    font-family:"Raleway",sans-serif;font-weight:300;font-size:34px;line-height:1.02;
    letter-spacing:1px;color:var(--rust);text-transform:uppercase;
  }
  .faq__list{position:absolute;left:34px;right:26px;top:150px;
    font-family:"Open Sans",sans-serif;font-style:italic;font-size:12px;line-height:1.36;color:var(--ink)}
  .faq__item{margin-bottom:8px}
  .faq__item:last-child{margin-bottom:0}
  .faq__q{font-weight:700;display:block}
  .faq__photo{
    position:absolute;left:0;right:0;bottom:0;height:250px;
    background:linear-gradient(160deg,#f7f4f0 0%,#e9d9c9 45%,#c99a85 80%,#d9b8a2 100%);
  }

  /* Inside back panel */
  .panel--back{background:var(--chocolate)}
  .back__shape{position:absolute;inset:0}
  .back__quote{
    position:absolute;left:34px;right:34px;top:48px;
    font-family:"Open Sans",sans-serif;font-style:italic;font-size:14px;line-height:1.55;color:#f3ebe2;
  }
  .back__cite{display:block;margin-top:12px;font-style:normal;font-weight:700;color:var(--khaki)}
  .back__motto{
    position:absolute;left:34px;right:34px;top:250px;
    font-family:"Raleway",sans-serif;font-weight:600;font-size:15px;letter-spacing:2px;color:var(--khaki);
  }
  .back__brand{position:absolute;left:40px;right:30px;top:560px}
  .brand{display:flex;align-items:center;gap:10px}
  .brand__dot{width:22px;height:22px;border-radius:50%;background:var(--gray);flex:none}
  .brand__name{font-family:"Raleway",sans-serif;font-weight:400;font-size:26px;color:var(--rust);line-height:1.05}
  .brand__tagline{font-family:"Raleway",sans-serif;font-weight:400;font-size:12px;color:var(--gray);letter-spacing:.5px;margin-top:6px}
  .contact{margin-top:22px;font-family:"Open Sans",sans-serif;font-size:13px;line-height:1.7;color:var(--chocolate)}
  .contact__row{display:flex;align-items:center;gap:8px}
  .contact__row svg{width:13px;height:13px;fill:var(--rust);flex:none}

  /* Cover panel */
  .panel--cover{background:var(--paper)}
  .cover__brand{position:absolute;left:44px;top:78px}
  .cover__brand .brand__name{font-size:34px}
  .cover__motto{
    position:absolute;left:126px;top:190px;
    font-family:"Raleway",sans-serif;font-weight:300;font-size:34px;line-height:1.02;color:var(--gray);
  }
  .cover__photo{
    position:absolute;left:0;right:0;bottom:0;height:500px;
    background:linear-gradient(180deg,#fbf8f4 0%,#efe3d3 30%,#d9c2a6 60%,#b8703d 88%,#8e4a22 100%);
  }
</style>
</head>
<body>
<main class="brochure">

  <section class="panel panel--faq">
    <h2 class="faq__title">Frequently<br>Asked<br>Questions</h2>
    <div class="faq__list">
      <p class="faq__item"><span class="faq__q">What can I expect at my appointment?</span>You can expect to be treated like family throughout the entire visit. We will respect your time and are dedicated to helping you better understand pro-active opioid education.</p>
      <p class="faq__item"><span class="faq__q">How long will my appointment last?</span>Please allow 45 minutes to complete your visit. (this allows time to complete your paperwork)</p>
      <p class="faq__item"><span class="faq__q">Will my information be kept confidential?</span>Yes, your visit will only be shared with your referring doctor. Hearthline Counseling is HIPAA Compliant.</p>
      <p class="faq__item"><span class="faq__q">Why do you need my ID and Insurance Card?</span>Your ID and insurance card are needed for verification and any lab tests that may be requested.</p>
      <p class="faq__item"><span class="faq__q">How much is my visit?</span>The office visit is only $40. (we have a hardship program for those in need)</p>
      <p class="faq__item"><span class="faq__q">Is this visit a one time appointment?</span>Hearthline sees patients 3 to 4 times a year Providing New Educational material and tools each time. (too much information for 1 visit)</p>
    </div>
    <div class="faq__photo" role="img" aria-label="Photo of a smiling senior couple, the man with white beard and glasses, the woman leaning on his shoulder"></div>
  </section>

  <section class="panel panel--back">
    <svg class="back__shape" viewBox="0 0 370 858" preserveAspectRatio="none" aria-hidden="true">
      <path d="M0 470 C120 430 260 450 370 500 L370 858 L0 858 Z" fill="#ffffff"/>
      <circle cx="60" cy="360" r="26" fill="#ffffff"/>
      <circle cx="150" cy="390" r="18" fill="#ffffff"/>
      <circle cx="250" cy="350" r="30" fill="#ffffff"/>
      <circle cx="330" cy="420" r="16" fill="#ffffff"/>
    </svg>
    <blockquote class="back__quote">
      “At first, I was reluctant about going to Hearthline. Once I got there, I was glad I went. I learned a lot and was treated like family the whole time.”
      <cite class="back__cite">— Marlene Oakes</cite>
    </blockquote>
    <p class="back__motto">MAKING SOLUTIONS ONE PATIENT AT A TIME</p>
    <div class="back__brand">
      <div class="brand"><span class="brand__dot"></span><span class="brand__name">Hearthline Counseling</span></div>
      <p class="brand__tagline">a pro-active opioid education center</p>
      <div class="contact">
        <p class="contact__row"><svg viewBox="0 0 24 24"><path d="M6.6 10.8a15.1 15.1 0 0 0 6.6 6.6l2.2-2.2a1 1 0 0 1 1-.25 11.4 11.4 0 0 0 3.6.57 1 1 0 0 1 1 1V20a1 1 0 0 1-1 1A17 17 0 0 1 3 4a1 1 0 0 1 1-1h3.5a1 1 0 0 1 1 1c0 1.25.2 2.45.57 3.6a1 1 0 0 1-.25 1z"/></svg>(555) 204-3318</p>
        <p class="contact__row"><svg viewBox="0 0 24 24"><path d="M12 2a7 7 0 0 0-7 7c0 5.25 7 13 7 13s7-7.750 7-13a7 7 0 0 0-7-7zm0 9.5A2.5 2.5 0 1 1 12 6.5a2.5 2.5 0 0 1 0 5z"/></svg>1420 Orchard Lane, Suite 3, Springfield</p>
        <p class="contact__row"><svg viewBox="0 0 24 24"><path d="M3 5h18v14H3zm2 2v.5l7 4.5 7-4.5V7l-7 4.5z"/></svg>info@hearthlinecounseling.com</p>
      </div>
    </div>
  </section>

  <section class="panel panel--cover">
    <div class="cover__brand">
      <div class="brand"><span class="brand__dot"></span><span class="brand__name">Hearthline Counseling</span></div>
      <p class="brand__tagline">a pro-active opioid education center</p>
    </div>
    <p class="cover__motto">making<br>solutions<br>"1" patient<br>at a time</p>
    <div class="cover__photo" role="img" aria-label="Photo of a smiling senior couple lying in autumn leaves outdoors"></div>
  </section>

</main>
</body>
</html>
```